Young, modern, highly skilled carpenter needs business card design

I need a business card design for my construction business. Its called 'Pellwright Construction Solutions'. Im looking for a ultra modern design that incorporates P C S, the first letters of the name with only a subtle reference to carpentry. The design should reflect my high quality work and eye for detail. i have also uploaded some exmaple designs i like.

Industry/Entity Type

Construction

Requirements
Must have
• Name of business, my name, mobile number, ABN number, email address
Nice to have
• A logo incorporating the name of the business

```html
<!DOCTYPE html>
<html lang="en">
<head>
<meta charset="utf-8">
<title>Pellwright Construction Solutions — Business Card</title>
<link rel="stylesheet" href="https://fonts.googleapis.com/css2?family=Nunito+Sans:wght@800&family=Crimson+Pro:wght@700&family=Noto+Sans:wght@400&display=swap">
<style>
  :root {
    --wood-dark: #6b3e14;
    --wood-mid: #9a6227;
    --wood-light: #b77c3a;
    --paper: #ffffff;
    --ink: #111111;
    --ink-soft: #1d2a2a;
    --accent: #b8864b;
    --muted: #a3a3a3;
    --shadow: #2a1a0a;
  }
  * { margin: 0; padding: 0; box-sizing: border-box; }
  html, body { width: 1200px; height: 719px; overflow: hidden; background: var(--paper); }
  .card { position: relative; width: 1200px; height: 719px; background: var(--paper); overflow: hidden; }

  .wood-band {
    position: absolute; left: 0; top: 0; width: 1200px; height: 248px;
    background: linear-gradient(180deg, var(--wood-mid) 0%, var(--wood-light) 35%, var(--wood-mid) 65%, var(--wood-dark) 100%);
  }
  .business-name {
    position: absolute; left: 0; top: 88px; width: 1200px; text-align: center;
    font-family: "Nunito Sans", sans-serif; font-weight: 800; font-size: 52px; letter-spacing: 1px;
    color: var(--paper); text-shadow: 4px 4px 0 var(--shadow);
  }
  .name-rule {
    position: absolute; left: 105px; top: 166px; width: 988px; height: 5px;
    background: var(--paper); box-shadow: 4px 4px 0 var(--shadow);
  }

  .services {
    position: absolute; left: 0; top: 272px; width: 1200px; text-align: center;
    font-family: "Crimson Pro", serif; font-weight: 700; font-size: 50px; color: var(--ink);
  }
  .services .dot { color: var(--accent); margin: 0 18px; font-size: 36px; vertical-align: 6px; }
  .services-note {
    position: absolute; left: 0; top: 344px; width: 1200px; text-align: center;
    font-family: "Crimson Pro", serif; font-weight: 700; font-size: 37px; color: var(--muted);
    padding-right: 80px;
  }
  .divider { position: absolute; left: 143px; top: 409px; width: 907px; height: 5px; background: var(--accent); }

  .monogram {
    position: absolute; left: 66px; top: 540px;
    font-family: "Noto Sans", sans-serif; font-weight: 400; font-size: 86px; line-height: 1;
    color: var(--ink); letter-spacing: 6px;
  }

  .contact { position: absolute; left: 0; top: 446px; width: 1200px; font-family: "Noto Sans", sans-serif; }
  .owner { position: absolute; left: 700px; top: 0; font-size: 39px; color: var(--ink-soft); letter-spacing: 1px; white-space: nowrap; }
  .row { position: absolute; left: 0; width: 1200px; font-size: 32px; white-space: nowrap; letter-spacing: 1px; }
  .row .label { position: absolute; right: 527px; color: var(--accent); }
  .row .value { position: absolute; left: 708px; color: var(--ink); }
  .row.mobile { top: 70px; }
  .row.email { top: 123px; }
  .row.abn { top: 181px; }
</style>
</head>
<body>
  <div class="card">
    <div class="wood-band" role="img" aria-label="Warm brown wood grain texture"></div>
    <h1 class="business-name">Pellwright Construction Solutions</h1>
    <div class="name-rule"></div>

    <p class="services">Decking<span class="dot">●</span>Housing<span class="dot">●</span>Pergolas</p>
    <p class="services-note">&amp; all other aspects of carpentry</p>
    <div class="divider"></div>

    <div class="monogram">P C S</div>

    <div class="contact">
      <p class="owner">Callum Pellwright</p>
      <p class="row mobile"><span class="label">m. no.</span><span class="value">9920451386</span></p>
      <p class="row email"><span class="label">email id.</span><span class="value">pellsolu@mailhub.com</span></p>
      <p class="row abn"><span class="label">ABN no.</span><span class="value">510298476631</span></p>
    </div>
  </div>
</body>
</html>
```